Bright Fern Accounting Postcard

I need a postcard that highlights my services and contact info. Please use the website for graphics/info... www.BrightFernAccounting.com

Target Market(s)

Business owners

Industry/Entity Type

Bookkeeper

Colors

Designer to choose colors to be used in the design.

Requirements
Must have
• Services listed, Certified Ledgerly Online Pro Advisor (can add Ledgerly logo), Contact info

```html
<!DOCTYPE html>
<html lang="en">
<head>
<meta charset="utf-8">
<title>Bright Fern Accounting Postcard</title>
<link href="https://fonts.googleapis.com/css2?family=Oswald:wght@500;600;700&family=Montserrat:wght@300;400;500&family=Noto+Serif:wght@700&family=Arimo:wght@400;700&display=swap" rel="stylesheet">
<style>
:root{
  --navy:#0d3a63;
  --navy-dark:#082a4a;
  --orange:#e87722;
  --orange-light:#f08a2c;
  --backdrop:#6b6b6b;
  --ink:#1d1d1d;
  --rule:#b9bfc6;
  --stamp:#d4d7da;
  --badge:#3f9c35;
}
*{margin:0;padding:0;box-sizing:border-box}
html,body{width:1200px;height:1200px;overflow:hidden}
body{background:var(--backdrop);position:relative;font-family:'Montserrat',sans-serif}
.card{position:absolute;width:745px;height:497px;background:#fff;overflow:hidden;box-shadow:0 3px 8px rgba(0,0,0,.35)}
.card--front{left:131px;top:91px}
.card--back{left:341px;top:606px}

/* shared brand line */
.brand{position:absolute;display:flex;align-items:center;gap:8px;font-family:'Noto Serif',serif;font-weight:700;color:var(--navy);white-space:nowrap}
.brand__mark{display:block;flex:none;background:var(--navy)}

/* front */
.front__skyline{position:absolute;left:190px;top:0;width:555px;height:400px;background:linear-gradient(90deg,#ffffff 0%,#eef0f3 40%,#e3e6ea 100%)}
.front__photo{position:absolute;left:0;top:0;width:745px;height:400px;background:linear-gradient(160deg,#123f6b 0%,#0b2f55 50%,#1a2a3c 100%);clip-path:polygon(378px 0,745px 0,745px 135px,720px 160px,745px 185px,745px 400px,355px 400px,470px 155px)}
.front__laptop{position:absolute;left:415px;top:175px;width:330px;height:290px;background:linear-gradient(170deg,#e8ebef 0%,#cfd4da 55%,#aab0b7 100%);clip-path:polygon(120px 0,330px 20px,330px 195px,250px 270px,20px 230px,0 215px,70px 175px)}
.card--front .brand{left:28px;top:66px;font-size:24px}
.card--front .brand__mark{width:22px;height:22px}
.headline{position:absolute;left:21px;top:122px;font-family:'Oswald',sans-serif;font-weight:700;font-size:84px;line-height:1;color:var(--navy);letter-spacing:2px;white-space:nowrap}
.subhead{position:absolute;left:21px;top:203px;font-family:'Montserrat',sans-serif;font-weight:300;font-size:36.5px;line-height:1.2;color:var(--orange);letter-spacing:0;white-space:nowrap}
.specialty{position:absolute;left:28px;top:258px;border-left:4px solid var(--navy);padding-left:17px;font-family:'Arimo',sans-serif;font-size:16px;line-height:19.5px;color:var(--ink)}
.specialty strong{display:block;font-weight:700}
.partner-badge{position:absolute;left:297px;top:281px;width:47px;height:47px;border-radius:50%;background:var(--badge)}
.front__bar{position:absolute;left:0;top:447px;width:745px;height:50px;background:var(--orange)}
.front__phone-tab{position:absolute;left:0;top:431px;width:281px;height:66px;background:var(--navy);clip-path:polygon(0 0,253px 0,281px 66px,0 66px)}
.front__phone{position:absolute;left:22px;top:442px;display:flex;align-items:center;gap:6px;font-family:'Oswald',sans-serif;font-weight:600;font-size:32px;color:#fff;white-space:nowrap}
.front__phone svg{width:18px;height:30px}
.front__contact{position:absolute;top:464px;display:flex;align-items:center;gap:8px;font-family:'Arimo',sans-serif;font-weight:700;font-size:12.6px;color:#fff;white-space:nowrap}
.front__contact svg{width:16px;height:14px}
.front__contact--mail{left:285px}
.front__contact--web{left:523px}

/* back */
.back__left{position:absolute;left:0;top:0;width:374px;height:497px;background:linear-gradient(180deg,#ffffff 30%,#eef1f5 100%)}
.back__photo{position:absolute;left:0;top:0;width:374px;height:94px;background:linear-gradient(100deg,#dfe9f5 0%,#a9c3e3 45%,#c9d9ee 100%)}
.back__stripe{position:absolute;left:0;top:92px;width:374px;height:3px;background:var(--orange)}
.back__laptop{position:absolute;left:175px;top:50px;width:180px;height:112px;background:linear-gradient(180deg,#3a3f46 0%,#f3f5f7 12%,#e9edf1 88%,#b6bcc3 100%);border-radius:4px}
.services-tab{position:absolute;left:14px;top:94px;width:96px;height:34px;background:var(--orange);font-family:'Oswald',sans-serif;font-weight:600;font-size:20px;color:#fff;text-align:center;line-height:34px;clip-path:polygon(0 0,100% 0,100% 82%,50% 100%,0 82%)}
.service{position:absolute;left:20px;width:340px}
.service__head{display:flex;align-items:center;gap:7px;font-family:'Oswald',sans-serif;font-weight:500;font-size:16px;color:var(--orange);margin-bottom:7px}
.service__head svg{width:20px;height:20px}
.service p{font-size:9.3px;line-height:11.2px;color:var(--ink);text-align:justify}
.service--books{top:155px}
.service--reports{top:260px}
.service--payroll{top:355px}
.back__bar{position:absolute;left:0;top:435px;width:374px;height:62px;background:var(--navy)}
.back__phone{position:absolute;left:20px;top:449px;display:flex;align-items:center;gap:12px;font-family:'Oswald',sans-serif;font-weight:500;font-size:21px;color:#fff;white-space:nowrap}
.back__phone svg{width:14px;height:26px}
.back__contact{position:absolute;left:198px;display:flex;align-items:center;gap:5px;font-size:8.6px;color:#fff;white-space:nowrap}
.back__contact svg{width:13px;height:10px}
.back__contact--mail{top:451px}
.back__contact--web{top:472px}
.stamp{position:absolute;left:654px;top:40px;width:58px;height:62px;background:var(--stamp)}
.address-line{position:absolute;left:418px;width:296px;height:1px;background:var(--rule)}
.card--back .brand{right:26px;top:451px;font-size:16.5px;gap:6px}
.card--back .brand__mark{width:15px;height:15px}
</style>
</head>
<body>

<section class="card card--front">
  <div class="front__skyline" role="img" aria-label="Faint photo of glass office towers"></div>
  <div class="front__photo" role="img" aria-label="Photo of dark blue glass skyscrapers seen from below"></div>
  <div class="front__laptop" role="img" aria-label="Photo of an open laptop showing an accounting dashboard"></div>

  <div class="brand"><span class="brand__mark"></span>Bright Fern Accounting</div>
  <h1 class="headline">BOUTIQUE</h1>
  <div class="subhead">ACCOUNTING FIRM</div>
  <div class="specialty">Specializing in
    <strong>Small Business Bookkeeping<br>&amp; Payroll Processing with<br>Ledgerly Online by Corvane.</strong>
  </div>
  <div class="partner-badge"></div>

  <div class="front__bar"></div>
  <div class="front__phone-tab"></div>
  <div class="front__phone">
    <svg viewBox="0 0 18 30"><path d="M7 1 C2 4 1 10 1 15 C1 20 2 26 7 29 L10 25 C7 23 6 19 6 15 C6 11 7 7 10 5 Z" fill="var(--orange)"/></svg>
    1.877.555.0142
  </div>
  <div class="front__contact front__contact--mail">
    <svg viewBox="0 0 16 12"><rect x=".5" y=".5" width="15" height="11" fill="none" stroke="#fff"/><path d="M.5 .5 L8 7 L15.5 .5" fill="none" stroke="#fff"/></svg>
    info@brightfernaccounting.com
  </div>
  <div class="front__contact front__contact--web">
    <svg viewBox="0 0 14 14"><circle cx="7" cy="7" r="6.3" fill="none" stroke="#fff"/><ellipse cx="7" cy="7" rx="2.8" ry="6.3" fill="none" stroke="#fff"/><path d="M.7 7 H13.3 M2 3.5 H12 M2 10.5 H12" stroke="#fff" fill="none"/></svg>
    www.brightfernaccounting.com
  </div>
</section>

<section class="card card--back">
  <div class="back__left"></div>
  <div class="back__photo" role="img" aria-label="Photo of business people signing papers at a desk"></div>
  <div class="back__stripe"></div>
  <div class="back__laptop" role="img" aria-label="Photo of a laptop showing a bookkeeping dashboard"></div>
  <div class="services-tab">SERVICES</div>

  <div class="service service--books">
    <h2 class="service__head">
      <svg viewBox="0 0 20 20"><ellipse cx="10" cy="5" rx="9" ry="4" fill="var(--navy)"/><path d="M1 8 Q10 13 19 8 V11 Q10 16 1 11 Z M1 13 Q10 18 19 13 V16 Q10 21 1 16 Z" fill="var(--navy)"/></svg>
      BOOKKEEPING</h2>
    <p>Let us take over the day to day bookkeeping so you can get back to running your business. We offer Ledgerly Online setup and ongoing bookkeeping, including daily journal entries, accounts payables &amp; receivables, bill pay, sales tax reporting &amp; payments, account reconciliation, and more.</p>
  </div>

  <div class="service service--reports">
    <h2 class="service__head">
      <svg viewBox="0 0 20 20" fill="none" stroke="var(--navy)" stroke-width="1.2"><rect x="5" y="1" width="14" height="18"/><rect x="1" y="6" width="8" height="13"/><path d="M8 5 H16 M11 9 H16 M11 12 H16 M3 10 H7 M3 13 H7 M3 16 H7"/></svg>
      FINANCIAL REPORTING</h2>
    <p>We'll provide easy to understand financial reports that allow you and your team to manage cash flow, create budgets and make forecasting decisions. Want real time data? Let us provide solutions with the latest in mobile apps and dashboards.</p>
  </div>

  <div class="service service--payroll">
    <h2 class="service__head">
      <svg viewBox="0 0 20 20" fill="none" stroke="var(--navy)" stroke-width="1.2"><circle cx="10" cy="4" r="2.5"/><circle cx="4" cy="7" r="2"/><circle cx="16" cy="7" r="2"/><path d="M6 19 V11 Q10 7 14 11 V19 M1 17 V12 Q4 9.5 6 11 M19 17 V12 Q16 9.5 14 11"/></svg>
      PAYROLL PROCESSING</h2>
    <p>Whether you have 5 employees or 100+, payroll can be an overwhelming and time consuming task. We offer full service payroll processing, including employee on boarding and reporting.</p>
  </div>

  <div class="back__bar"></div>
  <div class="back__phone">
    <svg viewBox="0 0 18 30"><path d="M7 1 C2 4 1 10 1 15 C1 20 2 26 7 29 L10 25 C7 23 6 19 6 15 C6 11 7 7 10 5 Z" fill="var(--orange)"/></svg>
    1.877.555.0142
  </div>
  <div class="back__contact back__contact--mail">
    <svg viewBox="0 0 16 12"><rect x=".5" y=".5" width="15" height="11" fill="none" stroke="#fff"/><path d="M.5 .5 L8 7 L15.5 .5" fill="none" stroke="#fff"/></svg>
    info@brightfernaccounting.com
  </div>
  <div class="back__contact back__contact--web">
    <svg viewBox="0 0 14 14"><circle cx="7" cy="7" r="6.3" fill="none" stroke="#fff"/><ellipse cx="7" cy="7" rx="2.8" ry="6.3" fill="none" stroke="#fff"/><path d="M.7 7 H13.3" stroke="#fff"/></svg>
    www.brightfernaccounting.com
  </div>

  <div class="stamp"></div>
  <div class="address-line" style="top:153px"></div>
  <div class="address-line" style="top:203px"></div>
  <div class="address-line" style="top:254px"></div>
  <div class="address-line" style="top:308px"></div>

  <div class="brand"><span class="brand__mark"></span>Bright Fern Accounting</div>
</section>

</body>
</html>
```